Remodel Flyer for realtors

"K" Tandem Builders

4"x 9" rack card front and back

www.BrindleyRenovator.com

555-318-4762

Let us fix what your home inspector finds!

Send us your inspection summary.

We are a licensed and Insured contractor.
CRC4871093

Serving
Marion County and The Heronfield

This flyer will sit in realtor offices for realtors to give to there buyers and sellers.

Target Market(s)

Realtors

Industry/Entity Type

Construction

Colors

Designer to choose colors to be used in the design.

```html
<!DOCTYPE html>
<html lang="en">
<head>
<meta charset="utf-8">
<title>"K" Tandem Builders Rack Card</title>
<link rel="stylesheet" href="https://fonts.googleapis.com/css2?family=Open+Sans:wght@400;600;700&family=Roboto+Condensed:wght@300;400;700&display=swap">
<style>
  :root{
    --bg:#d6d6d6;
    --white:#ffffff;
    --ink:#111111;
    --grey:#5a5b5e;
    --grey-mid:#6f7073;
    --orange:#f0922a;
    --orange-deep:#e0650f;
    --panel:#f0f1f1;
    --panel-edge:#d8dadb;
    --frame:#eeeeea;
    --dark:#242424;
    --black:#000000;
  }
  *{box-sizing:border-box;margin:0;padding:0}
  html,body{width:1140px;height:1200px;overflow:hidden;background:var(--bg)}
  body{position:relative;font-family:"Roboto Condensed",Arial,sans-serif}

  .card{position:absolute;top:60px;width:478px;height:1080px;overflow:hidden}
  .card--front{left:74px;background:var(--white)}
  .card--back{left:587px;background:var(--frame)}

  /* front */
  .brand{position:absolute;top:40px;left:0;width:100%;text-align:center}
  .brand__mark{width:72px;height:72px;background:var(--orange);margin:0 auto 22px}
  .brand__name{font-family:"Open Sans",Arial,sans-serif;font-weight:700;font-size:24px;letter-spacing:3px;color:var(--grey);text-transform:uppercase}
  .headline{position:absolute;top:228px;left:0;width:100%;text-align:center;font-family:"Open Sans",Arial,sans-serif;color:var(--grey);text-transform:uppercase}
  .headline__big{font-size:54px;font-weight:400;letter-spacing:7px;line-height:60px}
  .headline__mid{font-size:27px;letter-spacing:3.5px;line-height:36px}
  .headline__low{font-size:36px;letter-spacing:3.5px;line-height:46px}
  .accent{color:var(--orange);font-weight:700;font-style:italic}
  .front-photo{position:absolute;top:372px;left:0;width:100%;height:640px;
    background:linear-gradient(180deg,#ffffff 0%,#e9e4e0 25%,#7a6a62 45%,#3a3434 60%,#c8a08e 72%,#f3f2f0 88%,#ffffff 100%)}
  .front-cta{position:absolute;left:0;bottom:28px;width:100%;text-align:center;color:var(--ink)}
  .front-cta__note{font-size:17px;font-weight:400}
  .front-cta__phone{font-size:48px;font-weight:400;line-height:54px;margin-top:4px}
  .front-cta__url{font-size:20px;font-weight:400}

  /* back */
  .back-inner{position:absolute;left:29px;top:26px;width:422px;height:1024px;background:var(--panel-edge)}
  .room-photo{position:absolute;left:0;top:0;width:100%;height:338px;
    background:linear-gradient(120deg,#8d8377 0%,#d9d3c6 40%,#efe9dd 60%,#b08a66 100%)}
  .services{position:absolute;left:30px;top:0;width:138px;height:318px;background:var(--dark);color:var(--white);padding:30px 0 0 10px}
  .services__title{font-family:"Open Sans",Arial,sans-serif;font-size:23px;letter-spacing:2px;line-height:26px}
  .services__sub{font-family:"Open Sans",Arial,sans-serif;font-size:16px;letter-spacing:2px;display:block}
  .services__list{list-style:none;margin-top:44px}
  .services__list li{font-family:"Open Sans",Arial,sans-serif;font-size:14px;letter-spacing:1.5px;margin-bottom:14px}
  .services__list li::before{content:"";display:inline-block;width:3px;height:3px;background:var(--orange);margin-right:4px;vertical-align:middle}
  .info{position:absolute;left:30px;top:318px;width:366px;height:470px;background:var(--panel);text-align:center;color:var(--grey)}
  .info__title{font-family:"Open Sans",Arial,sans-serif;font-weight:700;font-size:36px;letter-spacing:4px;color:var(--orange-deep);margin-top:20px}
  .info__copy{font-size:14px;line-height:18px;text-align:justify;padding:0 22px;margin-top:14px;text-transform:uppercase}
  .info__copy + .info__copy{margin-top:14px}
  .info__license{font-size:15px;margin-top:26px;text-transform:uppercase}
  .info__code{font-weight:700;font-size:36px;color:var(--orange);line-height:40px}
  .info__rule{width:320px;height:1px;background:var(--orange);margin:18px auto 18px}
  .info__serving{font-weight:700;font-size:48px;color:var(--orange);line-height:48px}
  .info__area{font-size:21px;line-height:26px;text-transform:uppercase}
  .call{position:absolute;left:0;top:816px;width:100%;height:208px;background:var(--black);text-align:center;color:var(--white)}
  .call__label{font-weight:300;font-size:42px;line-height:78px}
  .call__phone{background:var(--orange);font-weight:700;font-size:58px;line-height:74px}
  .call__url{font-size:20px;font-weight:300;line-height:56px}
</style>
</head>
<body>
  <section class="card card--front">
    <div class="brand">
      <div class="brand__mark"></div>
      <div class="brand__name">"K" Tandem Builders</div>
    </div>
    <h1 class="headline">
      <div class="headline__big">Let us fix</div>
      <div class="headline__mid">What your <span class="accent">home</span></div>
      <div class="headline__low"><span class="accent">Inspector</span> finds!</div>
    </h1>
    <div class="front-photo" role="img" aria-label="Photo of a woman examining a small model house through a magnifying glass"></div>
    <div class="front-cta">
      <p class="front-cta__note">SEND US YOUR INSPECTION SUMMARY.</p>
      <p class="front-cta__phone">555-318-4762</p>
      <p class="front-cta__url">WWW.BRINDLEYRENOVATOR.COM</p>
    </div>
  </section>

  <section class="card card--back">
    <div class="back-inner">
      <div class="room-photo" role="img" aria-label="Photo of a bright remodeled bedroom"></div>
      <div class="services">
        <div class="services__title">PREMIUM<span class="services__sub">CONTRACTOR</span></div>
        <ul class="services__list">
          <li>KITCHENS</li>
          <li>BATHROOMS</li>
          <li>ADDITIONS</li>
          <li>WHOLE HOMES</li>
        </ul>
      </div>
      <div class="info">
        <h2 class="info__title">WELCOME</h2>
        <p class="info__copy">Whether it's getting your home remodeled or fixing damage that's been done to your home, we're here to help you every step of the way.</p>
        <p class="info__copy">At "K" Tandem Builders, we've built our livelihoods on remodeling people's homes. From the simple to the lavish, we've experienced it all and we can help you every step of the way.</p>
        <p class="info__license">We are a licensed and insured contractor.</p>
        <p class="info__code">CRC4871093</p>
        <div class="info__rule"></div>
        <p class="info__serving">SERVING</p>
        <p class="info__area">Marion County and<br>The Heronfield</p>
      </div>
      <div class="call">
        <p class="call__label">CALL US NOW</p>
        <p class="call__phone">555-318-4762</p>
        <p class="call__url">WWW.BRINDLEYRENOVATOR.COM</p>
      </div>
    </div>
  </section>
</body>
</html>
```